Flyer for teen fitness class at a physiotherapy clinic

We are a passionate Physiotherapy Clinic requiring a flyer to promote our new service a fitness class for teenagers, which is called Youth's FLX - Flexible Limber Xtra Power. The aim of the class is to prevents injuries in sports, improve sporting performance and provide safe activity for otherwise inactive teens. The aim of the flyer is to make people aware of this new service and interested in joining. Ideally the Flyer would incorporate blue colours. Our logo must be on the flier, and at least one or two of the photos provided. Our logo is provided in the attachments. Required information : Youth's FLX: Flexible Limber Xtra Power, times Mondays and Wednesdays 4 -5. Can be claimed on private health insurance. Expert advice to tailor a program to individual needs. For more information go www.rmpvq.com.au or phone 03)5871 6093.

Industry/Entity Type

Clinic

```html
<!DOCTYPE html>
<html lang="en">
<head>
<meta charset="utf-8">
<title>Youth's FLX Flyer</title>
<link href="https://fonts.googleapis.com/css2?family=Inter:wght@200;300;500;700;800;900&display=swap" rel="stylesheet">
<style>
  :root {
    --navy: #12264f;
    --blue: #2f82d0;
    --white: #ffffff;
    --ink: #1e1e1e;
    --grey: #8a8a8a;
    --stage: #e9e6df;
    --photo-gym: #b9b4ad;
    --photo-gym-dark: #5d5b58;
    --photo-sky: #8fb3d8;
    --photo-sky-dark: #6d6f7a;
  }
  * { margin: 0; padding: 0; box-sizing: border-box; }
  html, body { width: 1200px; height: 1026px; overflow: hidden; background: var(--stage); }
  body { position: relative; font-family: "Inter", Arial, sans-serif; }

  .flyer {
    position: absolute; left: 30px; top: 109px;
    width: 1140px; height: 808px;
    background: var(--navy); overflow: hidden;
  }
  .panel { position: absolute; background: var(--white); }
  .panel--main { left: 60px; top: 60px; width: 1020px; height: 688px; }
  .panel--top { left: 582px; top: 0; width: 558px; height: 306px; }

  .title {
    position: absolute; left: 126px; top: 108px;
    color: var(--blue); font-weight: 900;
    font-size: 122px; line-height: 104px; letter-spacing: -6px;
  }
  .subtitle {
    position: absolute; left: 126px; top: 322px;
    color: var(--grey); font-weight: 200;
    font-size: 76px; letter-spacing: -5px; white-space: nowrap;
  }

  .brand {
    position: absolute; left: 660px; top: 120px;
    display: flex; align-items: center; gap: 16px;
  }
  .brand__dot { width: 46px; height: 46px; border-radius: 50%; background: var(--blue); flex: none; }
  .brand__name {
    color: var(--navy); font-weight: 800; font-size: 40px; line-height: 44px; letter-spacing: -1px;
  }

  .schedule {
    position: absolute; left: 128px; top: 428px;
    font-weight: 700; font-size: 21px; color: var(--ink);
  }
  .rule {
    position: absolute; left: 128px; top: 463px; width: 882px; height: 1.5px; background: var(--navy);
  }
  .benefits {
    position: absolute; left: 128px; top: 478px; width: 340px;
    list-style: none; font-size: 21px; line-height: 26px; color: var(--ink);
  }
  .benefits li { padding-left: 22px; position: relative; margin-bottom: 10px; }
  .benefits li::before {
    content: ""; position: absolute; left: 3px; top: 10px;
    width: 8px; height: 8px; border-radius: 50%; background: var(--blue);
  }
  .contact {
    position: absolute; left: 134px; top: 630px;
    color: var(--blue); font-size: 21px; line-height: 27px;
  }
  .contact strong { font-weight: 700; }

  .art { position: absolute; left: 0; top: 0; width: 1140px; height: 808px; }
</style>
</head>
<body>
  <main class="flyer">
    <div class="panel panel--main"></div>
    <div class="panel panel--top"></div>

    <h1 class="title">Youth's<br>FLX:</h1>
    <p class="subtitle">Flexible Limber Xtra Power</p>

    <div class="brand">
      <span class="brand__dot"></span>
      <span class="brand__name">Harbourline<br>Sports Physio</span>
    </div>

    <p class="schedule">Mondays and Wednesdays 4 - 5.</p>
    <div class="rule"></div>
    <ul class="benefits">
      <li>Can be claimed on private health insurance.</li>
      <li>Expert advice to tailor a program to individual needs.</li>
    </ul>
    <p class="contact">For more information go<br><strong>www.rmpvq.com.au</strong> or<br><strong>phone 03 5871 6093.</strong></p>

    <svg class="art" viewBox="0 0 1140 808" aria-hidden="false">
      <defs>
        <linearGradient id="gym" x1="0" y1="0" x2="0" y2="1">
          <stop offset="0" stop-color="var(--photo-gym)"/>
          <stop offset="1" stop-color="var(--photo-gym-dark)"/>
        </linearGradient>
        <linearGradient id="sky" x1="0" y1="0" x2="0" y2="1">
          <stop offset="0" stop-color="var(--photo-sky)"/>
          <stop offset="1" stop-color="var(--photo-sky-dark)"/>
        </linearGradient>
      </defs>
      <g class="accents" fill="var(--navy)">
        <polygon points="750,417 788,417 772,470 734,470"/>
        <polygon points="910,472 928,472 922,494 904,494"/>
        <polygon points="942,488 982,488 966,542 926,542"/>
        <polygon points="420,612 505,612 483,712 404,712"/>
        <polygon points="756,548 792,548 778,602 742,602"/>
      </g>
      <g fill="var(--blue)">
        <polygon points="780,434 792,434 789,450 777,450"/>
        <polygon points="424,704 440,704 437,722 421,722"/>
        <polygon points="1106,534 1118,534 1114,550 1102,550"/>
      </g>
      <polygon class="photo" role="img" aria-label="Photo of a teenager training in the clinic gym with a physiotherapist" fill="url(#gym)" points="523,424 812,424 722,808 430,808"/>
      <polygon class="photo" role="img" aria-label="Photo of two teens jumping outdoors" fill="url(#sky)" points="790,582 968,582 925,772 760,772"/>
      <polygon class="photo" role="img" aria-label="Photo of a teen catching a netball outdoors" fill="url(#sky)" points="977,514 1112,514 1088,692 952,692"/>
      <polygon fill="var(--blue)" points="938,684 956,684 950,704 932,704"/>
      <polygon fill="var(--navy)" points="1040,684 1062,684 1054,706 1032,706"/>
    </svg>
  </main>
</body>
</html>
```